WordPress website in children books redesign

We are personalised children storybook creators with a range of personalized books, music CDs and DVDs that are created for each child. We sell our concept through a license via distributors / entrepreneurs mainly based in France and Europe. We want to focus on selling B2C to parents and grandparents, looking to buy presents to their children aged 0 to 10 years old. Those present are educative, unique for each child, and they will learn to have fun and learn to have fun. I would like to redesign our WordPress website https://brightpebbletales.co.uk/index.php We are a children in the world of books and music books: books, music CDs and DVDs looking for something a little more along the lines of our competitors. See ike www.glimmerpage.com, www.tovikoro.com, www.lefiletdesetoiles.com, https://www.lespetitsvergers.com/, https://plumquestkids.com/ Our current website is a bit too old fashioned so I am looking at a much more modern design Here is a link for a few products that are not available here: https://www.filecrate.example/sh/kq417ptobnrelwx/ZZQ4rTfLmN8y-aBcDeFgHiJ-kl?dl=0 We have 2 sides in our website: B2C on the left side and B2B on the right site; B2B is for distributors that are entrepreneurs buying our concept. for the homepage design, the main focus will be B2Consumer Our current page is too blended, lacks reassurance elements and I would like to have a look at this page. from our current stories. here is a link for our business book to give you a feel for it: http://online.pagewhirl.example/qtpd/mnvs/ MAIN PAGES TO REVIEW / HOMEPAGE / https://brightpebbletales.co.uk/ BOOKS: https : //brightpebbletales.co.uk/product-category/personalised-books/ MUSIC: https://brightpebbletales.co.uk/product-category/music-cds/ BLOG: https://brightpebbletales.co.uk/blog -2 / Looking forward to seeing you and your questions asap

Target Market(s)

parents and grandparents of children aged 0 to 10 years old. This is for the European market

Industry/Entity Type

Publishing Company

Number of Pages Required

4 page

Colors
0392cd
9bcb3b
ec1f27
757575

Requirements
Must have
• keep within the color code of our RGB logo: D25028 RGB: 8CC364 329BC8 808285
Nice to have
• be more with the style of our competitors. Bright Pebble Tales am about making children learn the fun way, and develop their morality, self-esteem and confidence. It's about the magic of reading to help children learn while having fun. I have attached visuals but those are just examples and you we encourage you to suggest other ideas

```html
<!DOCTYPE html>
<html lang="en">
<head>
<meta charset="utf-8">
<title>Bright Pebble Tales – Personalised Children's Books</title>
<link rel="stylesheet" href="https://fonts.googleapis.com/css2?family=Open+Sans:wght@400;600;700&family=Sniglet&family=Pacifico&display=swap">
<style>
:root{
  --blue:#0392cd;
  --green:#9bcb3b;
  --red:#ec1f27;
  --grey:#757575;
  --orange:#d25028;
  --yellow:#f6c21c;
  --cream:#fffbd6;
  --ink:#333333;
  --dark:#1b2124;
  --black:#0c0f10;
  --sky:#c9ecf6;
  --white:#ffffff;
  --body:"Open Sans", Arial, sans-serif;
  --title:"Sniglet", "Trebuchet MS", sans-serif;
  --script:"Pacifico", cursive;
}
*{box-sizing:border-box;margin:0;padding:0}
html,body{width:1200px;height:3696px;overflow:hidden}
body{position:relative;font-family:var(--body);color:var(--ink);background:var(--white)}
.abs{position:absolute}
.section-title{position:absolute;left:0;width:1200px;text-align:center;font-family:var(--title);font-size:34px;color:var(--red);letter-spacing:1px}
.section-title .squiggle{display:block;margin:6px auto 0}

/* top bar */
.promo-bar{top:0;left:0;width:1200px;height:37px;background:var(--black);color:var(--white);font-size:9px}
.promo-bar p{position:absolute;left:132px;top:12px}
.promo-bar .promo-code{position:absolute;left:566px;top:9px;background:var(--red);color:var(--white);font-size:8px;font-weight:700;padding:4px 12px;border-radius:3px}

/* nav */
.site-nav{top:37px;left:0;width:1200px;height:86px;background:var(--white)}
.brand{position:absolute;left:128px;top:16px;display:flex;align-items:center;gap:8px}
.brand .mark{width:18px;height:18px;border-radius:50%;background:var(--red)}
.brand span{font-family:var(--title);font-size:15px;color:var(--red);width:70px;line-height:1.1}
.menu a{position:absolute;top:36px;font-size:14px;color:var(--ink);text-decoration:none}
.menu a.active::after{content:"";position:absolute;left:0;right:0;bottom:-8px;height:3px;background:var(--yellow);border-radius:2px}
.cart{position:absolute;left:985px;top:33px;font-size:14px;display:flex;align-items:center;gap:8px}

/* hero */
.hero{top:123px;left:0;width:1200px;height:500px;overflow:hidden}
.hero .photo{position:absolute;inset:0;background:linear-gradient(110deg,#c9314a 0%,#e6643b 25%,#5c8fd4 50%,#e5b34a 72%,#3a64b3 100%)}
.ribbon{position:absolute;color:var(--white);font-family:var(--script);white-space:nowrap;line-height:1}
.ribbon.r1{left:217px;top:30px;width:400px;height:86px;background:var(--orange);font-size:60px;padding:8px 0 0 36px;transform:rotate(-2deg)}
.ribbon.r2{left:163px;top:95px;width:160px;height:46px;background:var(--green);font-size:36px;padding:2px 0 0 20px}
.ribbon.r3{left:308px;top:100px;width:505px;height:98px;background:var(--blue);font-size:64px;padding:10px 0 0 30px;transform:rotate(-1deg)}
.hero .plane{position:absolute;left:0;top:410px;width:180px;height:100px;border-radius:40px;background:linear-gradient(90deg,#e54a9a,#f2a3cf)}
.hero .wave{position:absolute;left:0;bottom:0}

/* vision & mission */
.about-col{position:absolute;top:675px;width:432px}
.about-col h2{font-family:var(--title);font-weight:400;font-size:32px;color:var(--red);text-align:center}
.about-col p{margin-top:28px;font-size:12.5px;line-height:19px;color:var(--ink)}
.balloon{position:absolute;left:1060px;top:640px;width:140px;height:200px;border-radius:70px 70px 40px 40px;background:linear-gradient(90deg,#f7d23a,#43b7e6,#ec4aa0,#f28b2e)}

/* offer */
.offer-card{position:absolute;top:1035px;width:271px}
.offer-card .pic{height:259px}
.offer-card .btn{display:block;margin:14px auto 0;width:262px;height:52px;border-radius:6px;background:var(--red);color:var(--white);font-size:18px;font-weight:600;text-align:center;line-height:52px}

/* distributors */
.distributors{top:1400px;left:0;width:1200px;height:660px}
.distributors .band{position:absolute;left:0;top:0}
.distributors .section-title{top:76px;color:var(--white)}
.price-card{position:absolute;text-align:center;border-radius:6px}
.price-card.side{top:177px;height:360px;width:290px;background:var(--cream)}
.price-card.feature{top:170px;left:441px;width:311px;height:372px;background:var(--white);box-shadow:0 6px 24px rgba(0,0,0,.25);z-index:2}
.price-card h3{margin-top:40px;font-family:var(--title);font-weight:400;font-size:19px;color:var(--green)}
.price-card .price{margin-top:14px;font-size:30px;color:var(--red);font-weight:400}
.price-card ul{list-style:none;text-align:left;margin:14px 0 0 36px;font-size:12px;line-height:17px;color:var(--ink)}
.price-card li{position:relative;padding-left:16px}
.price-card li::before{content:"";position:absolute;left:0;top:6px;width:6px;height:6px;border-radius:50%;background:var(--green)}
.price-card .purchase{position:absolute;left:50%;transform:translateX(-50%);bottom:40px;width:124px;height:40px;line-height:40px;background:var(--red);color:var(--white);font-size:13px;border-radius:4px}
.best-offer{position:absolute;left:441px;top:1570px;width:37px;height:120px;background:var(--yellow);z-index:3;clip-path:polygon(0 0,100% 0,100% 100%,50% 86%,0 100%)}
.best-offer span{position:absolute;left:8px;top:84px;transform:rotate(-90deg);transform-origin:left top;color:var(--white);font-size:12px;white-space:nowrap}
.bear{position:absolute;left:1018px;top:1505px;width:120px;height:140px;border-radius:50%;background:linear-gradient(135deg,#9a5a2b,#6fae3c)}
.backpack{position:absolute;left:128px;top:1790px;width:82px;height:110px;border-radius:30px 30px 14px 14px;background:linear-gradient(160deg,#3b8fd8,#f2a41c)}

/* blogs */
.blogs{top:2045px;left:0;width:1200px;height:640px;background:linear-gradient(180deg,#fdf1ee 0%,#fbeaf2 50%,#fdf1ee 100%)}
.blogs .section-title{top:42px}
.blog-bubble{position:absolute;top:150px;width:282px;height:240px}
.blog-bubble svg{position:absolute;inset:0}
.blog-bubble p{position:absolute;left:20px;top:84px;width:244px;color:var(--white);font-size:12.5px;line-height:18px}
.blog-author{position:absolute;top:466px;width:282px;text-align:center;font-family:var(--title);font-size:24px}
.snail{position:absolute;left:905px;top:45px;width:100px;height:70px;border-radius:40px 40px 10px 10px;background:linear-gradient(90deg,#f28b2e,#8cc364)}
.girl{position:absolute;left:52px;top:370px;width:100px;height:240px;border-radius:40px;background:linear-gradient(180deg,#e8352c,#f6b6c8,#f6c44a)}

/* contact */
.contact{top:2670px;left:0;width:1200px;height:565px}
.contact .photo{position:absolute;inset:0;background:linear-gradient(120deg,#b4306e 0%,#e1579a 30%,#f4a5c8 55%,#d84a8a 80%,#9f2a63 100%)}
.contact-panel{position:absolute;left:357px;top:35px;width:488px;height:461px;background:rgba(255,255,255,.9);border-radius:4px}
.contact-panel h2{margin-top:18px;text-align:center;font-family:var(--title);font-weight:400;font-size:28px;color:var(--red)}
.field{position:absolute;left:45px;width:400px;height:35px;background:var(--white);border:1px solid #d8d8d8;border-radius:3px;font-size:11px;color:#aaa;padding:11px 12px}
.field.half{width:192px}
.send-query{position:absolute;left:45px;top:397px;width:400px;height:40px;line-height:40px;text-align:center;background:var(--red);color:var(--white);font-size:14px;border-radius:4px}

/* partners */
.partners{top:3230px;left:0;width:1200px;height:178px;background:var(--sky)}
.partner{position:absolute;top:78px;width:64px;height:54px;border-radius:50%;background:rgba(3,146,205,.35)}

/* footer */
.site-footer{top:3408px;left:0;width:1200px;height:263px;background:var(--dark);color:var(--white)}
.footer-brand{position:absolute;left:130px;top:26px;display:flex;align-items:center;gap:8px}
.footer-brand .mark{width:16px;height:16px;border-radius:50%;background:var(--red)}
.footer-brand span{font-family:var(--title);font-size:14px;color:var(--white);width:66px;line-height:1.1}
.footer-about{position:absolute;left:130px;top:100px;width:240px;font-size:12px;line-height:15px}
.footer-col{position:absolute;top:40px}
.footer-col h4{font-family:var(--title);font-weight:400;font-size:20px;color:var(--red)}
.footer-col ul{list-style:none;margin-top:36px;font-size:12px;line-height:32px}
.newsletter-input{position:absolute;left:830px;top:110px;width:237px;height:35px;background:#2c3236;font-size:12px;padding:10px 14px}
.newsletter-send{position:absolute;left:968px;top:165px;width:119px;height:40px;line-height:40px;text-align:center;background:var(--red);font-size:13px;border-radius:3px}
.legal-bar{top:3671px;left:0;width:1200px;height:25px;background:var(--black);color:var(--white);font-size:8px}
.legal-bar p{position:absolute;left:132px;top:8px}
</style>
</head>
<body>

<header class="abs promo-bar">
  <p>Woohoo! 15% off every book, CD and DVD this week (distributor packs not included)</p>
  <span class="promo-code">WOOHOO</span>
</header>

<nav class="abs site-nav">
  <div class="brand"><i class="mark"></i><span>Bright Pebble Tales</span></div>
  <div class="menu">
    <a class="active" style="left:344px">Welcome</a>
    <a style="left:449px">Our Products</a>
    <a style="left:578px">About Us</a>
    <a style="left:685px">Distributors</a>
    <a style="left:812px">Blog</a>
    <a style="left:886px">Contact</a>
  </div>
  <div class="cart">
    <svg width="20" height="18" viewBox="0 0 20 18" fill="none" stroke="#333" stroke-width="1.6"><path d="M1 2h3l2.5 10h10l2-7H5.5"/><circle cx="8" cy="15.5" r="1.4"/><circle cx="15" cy="15.5" r="1.4"/></svg>
    <span>0 items</span>
  </div>
</nav>

<section class="abs hero">
  <div class="photo" role="img" aria-label="Photo of happy children cheering with raised arms in a colourful soft play room"></div>
  <h1>
    <span class="ribbon r1">Who wants</span>
    <span class="ribbon r2">to be</span>
    <span class="ribbon r3">a Superhero ?</span>
  </h1>
  <div class="plane" role="img" aria-label="Illustration of a pink toy aeroplane"></div>
  <svg class="wave" width="1200" height="30" viewBox="0 0 1200 30" preserveAspectRatio="none">
    <path fill="#fff" d="M0 30V14 Q15 0 30 14 Q45 0 60 14 Q75 0 90 14 Q105 0 120 14 Q135 0 150 14 Q165 0 180 14 Q195 0 210 14 Q225 0 240 14 Q255 0 270 14 Q285 0 300 14 Q315 0 330 14 Q345 0 360 14 Q375 0 390 14 Q405 0 420 14 Q435 0 450 14 Q465 0 480 14 Q495 0 510 14 Q525 0 540 14 Q555 0 570 14 Q585 0 600 14 Q615 0 630 14 Q645 0 660 14 Q675 0 690 14 Q705 0 720 14 Q735 0 750 14 Q765 0 780 14 Q795 0 810 14 Q825 0 840 14 Q855 0 870 14 Q885 0 900 14 Q915 0 930 14 Q945 0 960 14 Q975 0 990 14 Q1005 0 1020 14 Q1035 0 1050 14 Q1065 0 1080 14 Q1095 0 1110 14 Q1125 0 1140 14 Q1155 0 1170 14 Q1185 0 1200 14V30Z"/>
  </svg>
</section>

<section class="about">
  <article class="about-col" style="left:148px">
    <h2>Our Vision</h2>
    <p>is to make children the heroes of the adventure and live magical and unforgettable moments they can share with their family and friends. Scenarios are adapted to every age, imagined and conceived in association with children, schools, speech therapists, psychologists and childhood experts.</p>
  </article>
  <article class="about-col" style="left:628px">
    <h2>Our Mission</h2>
    <p>Personalisation offers for children to have an opportunity to recognise themselves in the story, thus developing the morale, self-esteem and confidence. All our stories aim to stimulate learning and enhance reading passion from an early age and have been designed with high-quality original artwork with bright colours to fully engage a child's imagination. The stories are written in an educational and informative way, whilst remaining fun, positive, and engaging.</p>
  </article>
  <div class="balloon" role="img" aria-label="Illustration of a striped hot air balloon"></div>
</section>

<section class="offer">
  <h2 class="section-title" style="top:932px">What We Offer
    <svg class="squiggle" width="60" height="10" viewBox="0 0 60 10"><path d="M2 7 Q9 1 16 7 T30 7 T44 7 T58 7" fill="none" stroke="#f6c21c" stroke-width="2.5" stroke-linecap="round"/></svg>
  </h2>
  <div class="offer-card" style="left:133px">
    <div class="pic" role="img" aria-label="Photo of a smiling boy holding his personalised storybook" style="background:linear-gradient(135deg,#7c8f5a,#c9a46a,#3f6aa8)"></div>
    <span class="btn">Personalized Books</span>
  </div>
  <div class="offer-card" style="left:463px">
    <div class="pic" role="img" aria-label="Photo of a girl listening to music with headphones against an orange wall" style="background:linear-gradient(135deg,#f08a1c,#f6a23a,#4fa9d8)"></div>
    <span class="btn">Music</span>
  </div>
  <div class="offer-card" style="left:796px">
    <div class="pic" role="img" aria-label="Photo of two children watching a laptop screen" style="background:linear-gradient(135deg,#8a97a4,#d8cfc3,#5d6f82)"></div>
    <span class="btn">DVDs</span>
  </div>
</section>

<section class="abs distributors">
  <svg class="band" width="1200" height="660" viewBox="0 0 1200 660" preserveAspectRatio="none">
    <path fill="#0392cd" d="M0 20 Q20 0 40 20 Q60 0 80 20 Q100 0 120 20 Q140 0 160 20 Q180 0 200 20 Q220 0 240 20 Q260 0 280 20 Q300 0 320 20 Q340 0 360 20 Q380 0 400 20 Q420 0 440 20 Q460 0 480 20 Q500 0 520 20 Q540 0 560 20 Q580 0 600 20 Q620 0 640 20 Q660 0 680 20 Q700 0 720 20 Q740 0 760 20 Q780 0 800 20 Q820 0 840 20 Q860 0 880 20 Q900 0 920 20 Q940 0 960 20 Q980 0 1000 20 Q1020 0 1040 20 Q1060 0 1080 20 Q1100 0 1120 20 Q1140 0 1160 20 Q1180 0 1200 20 V645 H0Z"/>
  </svg>
  <h2 class="section-title">Distributors
    <svg class="squiggle" width="60" height="10" viewBox="0 0 60 10"><path d="M2 7 Q9 1 16 7 T30 7 T44 7 T58 7" fill="none" stroke="#f6c21c" stroke-width="2.5" stroke-linecap="round"/></svg>
  </h2>
</section>

<div class="best-offer"><span>Best Offer</span></div>
<div class="abs" style="top:1400px;left:0;width:1200px;height:660px;z-index:1">
  <div class="price-card side" style="left:155px">
    <h3>Platinum Pack</h3>
    <div class="price">£ 3,890</div>
    <ul>
      <li>Mix of 100 books</li>
      <li>Mix of 100 poems/letters</li>
      <li>100 StoryNest Premium membership</li>
      <li>100 CD downloads</li>
      <li>100 recordable heart modules</li>
      <li>Unlimited eBooks and activity books (games &amp; colouring books) downloads</li>
    </ul>
    <span class="purchase">Purchase</span>
  </div>
  <div class="price-card feature">
    <h3>Discovery Pack</h3>
    <div class="price">£ 999,00</div>
    <ul>
      <li>Mix of 50 books</li>
      <li>Mix of 50 poems/letters</li>
      <li>50 StoryNest Premium membership</li>
      <li>Unlimited eBooks and activity books (games &amp; colouring books) downloads</li>
    </ul>
    <span class="purchase">Purchase</span>
  </div>
  <div class="price-card side" style="left:752px">
    <h3>Gold Pack</h3>
    <div class="price">£ 2,490</div>
    <ul>
      <li>Mix of 100 books</li>
      <li>Mix of 100 poems/letters</li>
      <li>100 StoryNest Premium membership</li>
      <li>10 CD downloads</li>
      <li>10 heart recordable modules</li>
      <li>Unlimited eBooks and activity books (games &amp; colouring books) downloads</li>
    </ul>
    <span class="purchase">Purchase</span>
  </div>
</div>
<div class="bear" role="img" aria-label="Illustration of a teddy bear hanging from a leafy branch" style="z-index:2"></div>
<div class="backpack" role="img" aria-label="Illustration of a school backpack" style="z-index:3"></div>

<section class="abs blogs">
  <h2 class="section-title">Blogs
    <svg class="squiggle" width="60" height="10" viewBox="0 0 60 10"><path d="M2 7 Q9 1 16 7 T30 7 T44 7 T58 7" fill="none" stroke="#f6c21c" stroke-width="2.5" stroke-linecap="round"/></svg>
  </h2>
  <div class="snail" role="img" aria-label="Illustration of a snail"></div>

  <div class="blog-bubble" style="left:131px">
    <svg width="282" height="240" viewBox="0 0 282 240"><path fill="#9bcb3b" d="M14 40 Q14 24 30 24 H70 Q80 0 110 8 Q130 -4 150 14 Q170 4 190 22 H266 Q280 22 280 38 V206 Q280 222 264 222 H30 Q14 222 14 206Z"/><circle cx="100" cy="232" r="7" fill="#9bcb3b"/></svg>
    <p>I am text block. Click edit button to change this text. Lorem ipsum dolor sit amet, consectetur adipiscing elit. Ut elit tellus, luctus nec ullamcorper mattis, pulvinar dapibus leo.</p>
  </div>
  <div class="blog-bubble" style="left:463px">
    <svg width="282" height="240" viewBox="0 0 282 240"><path fill="#ec1f27" d="M4 40 Q4 24 20 24 H90 Q100 0 130 4 Q150 -4 170 10 Q190 4 200 22 H256 Q272 22 272 38 V200 Q272 216 256 216 H20 Q4 216 4 200Z"/><circle cx="110" cy="228" r="9" fill="#ec1f27"/><circle cx="130" cy="236" r="4" fill="#ec1f27"/></svg>
    <p>I am text block. Click edit button to change this text. Lorem ipsum dolor sit amet, consectetur adipiscing elit. Ut elit tellus, luctus nec ullamcorper mattis, pulvinar dapibus leo.</p>
  </div>
  <div class="blog-bubble" style="left:793px">
    <svg width="282" height="240" viewBox="0 0 282 240"><path fill="#0392cd" d="M4 40 Q4 24 20 24 H100 Q120 2 150 10 Q170 0 188 18 H260 Q276 18 276 34 V206 Q276 222 260 222 H20 Q4 222 4 206Z"/><circle cx="230" cy="232" r="7" fill="#0392cd"/></svg>
    <p style="top:72px">I am text block. Click edit button to change this text. Lorem ipsum dolor sit amet, consectetur adipiscing elit. Ut elit tellus, luctus nec ullamcorper mattis, pulvinar dapibus leo.</p>
  </div>

  <div class="blog-author" style="left:131px;color:#9bcb3b">Lily Rowan</div>
  <div class="blog-author" style="left:463px;color:#ec1f27">Lily Rowan</div>
  <div class="blog-author" style="left:793px;color:#0392cd">Lily Rowan</div>
  <div class="girl" role="img" aria-label="Illustration of a little girl holding a red balloon"></div>

  <svg class="abs" style="left:0;top:600px" width="1200" height="40" viewBox="0 0 1200 40" preserveAspectRatio="none">
    <path fill="#9bcb3b" d="M0 40V16 Q25 0 50 16 Q75 0 100 16 Q125 0 150 16 Q175 0 200 16 Q225 0 250 16 Q275 0 300 16 Q325 0 350 16 Q375 0 400 16 Q425 0 450 16 Q475 0 500 16 Q525 0 550 16 Q575 0 600 16 Q625 0 650 16 Q675 0 700 16 Q725 0 750 16 Q775 0 800 16 Q825 0 850 16 Q875 0 900 16 Q925 0 950 16 Q975 0 1000 16 Q1025 0 1050 16 Q1075 0 1100 16 Q1125 0 1150 16 Q1175 0 1200 16V40Z"/>
  </svg>
</section>

<section class="abs contact">
  <div class="photo" role="img" aria-label="Photo of a wrapped gift tied with a pink satin ribbon"></div>
  <form class="contact-panel">
    <h2>Contact Us</h2>
    <div class="field half" style="top:111px">First Name</div>
    <div class="field half" style="top:111px;left:253px">Last Name</div>
    <div class="field" style="top:163px"></div>
    <div class="field" style="top:212px">Phone Number</div>
    <div class="field" style="top:261px;height:102px">Message</div>
    <span class="send-query">Send Your Querry</span>
  </form>
</section>

<section class="abs partners" aria-label="Partners">
  <span class="partner" style="left:166px"></span>
  <span class="partner" style="left:357px"></span>
  <span class="partner" style="left:571px"></span>
  <span class="partner" style="left:775px"></span>
  <span class="partner" style="left:965px"></span>
</section>

<footer class="abs site-footer">
  <div class="footer-brand"><i class="mark"></i><span>Bright Pebble Tales</span></div>
  <p class="footer-about">Lorem ipsum dolor sit amet, consectetur adipiscing elit, sed do eiusmod tempor incididunt ut labore et dolore magna aliqua. Ut enim ad minim veniam, quis nostrud exercitation ullamco laboris nisi ut aliquip ex ea commodo consequat.</p>
  <div class="footer-col" style="left:406px">
    <h4>Our Collection</h4>
    <ul><li>Personalised books</li><li>Personalised music albums</li><li>Personalised DVD cartoon</li><li>Personalised school books</li></ul>
  </div>
  <div class="footer-col" style="left:633px">
    <h4>Distributors</h4>
    <ul><li>Discovery pack</li><li>Gold pack</li><li>Platinum pack</li><li>Success stories</li></ul>
  </div>
  <div class="footer-col" style="left:835px">
    <h4>News Letter</h4>
  </div>
  <div class="newsletter-input">Your Email</div>
  <span class="newsletter-send">Send</span>
</footer>

<div class="abs legal-bar"><p>© Bright Pebble Tales - All rights reserved</p></div>

</body>
</html>
```